Kestrim LLC, needs a web page no more than 5 pages (for now)

Kestrim is a general contractor. Our services include general contracting, design-build construction, disaster recovery and environmental remediation. Our main clients are KZE, HJ, State and Local Gov't Agencies, Hospitals and Schools. Kestrim is also a SDVOSB.

```html
<!DOCTYPE html>
<html lang="en">
<head>
<meta charset="utf-8">
<title>Kestrim LLC — General Contractor</title>
<link href="https://fonts.googleapis.com/css2?family=Montserrat:ital,wght@0,400;0,500;0,600;0,700;1,400&family=Montserrat+Alternates:wght@500&display=swap" rel="stylesheet">
<style>
:root{
  --black:#000;
  --ink:#0d0d0d;
  --panel:#141414;
  --white:#fff;
  --muted:#cfcfcf;
  --gold:#d4a829;
  --gold-light:#f1d46a;
  --gold-dark:#9a7414;
  --gold-grad:linear-gradient(180deg,#f0d36a 0%,#c9a02c 55%,#a57d1a 100%);
}
*{margin:0;padding:0;box-sizing:border-box}
html,body{width:1200px;height:5150px;overflow:hidden;background:var(--black)}
body{position:relative;font-family:"Montserrat",sans-serif;color:var(--white)}
.abs{position:absolute}
.btn{position:absolute;display:flex;align-items:center;justify-content:center;background:var(--gold-grad);color:#1a1200;font-weight:600;font-size:13px;letter-spacing:.3px;box-shadow:0 3px 8px rgba(0,0,0,.5)}
.section-title{position:absolute;font-weight:600;font-size:40px;letter-spacing:-.5px}
.rule{position:absolute;height:3px;width:84px;background:var(--gold)}
.rule::before,.rule::after{content:"";position:absolute;top:-2px;width:7px;height:7px;border-radius:50%;background:var(--gold)}
.rule::before{left:-3px}.rule::after{right:-3px}
.center{left:0;width:1200px;text-align:center}

/* header */
.site-header{left:0;top:0;width:1200px;height:122px;background:var(--black)}
.brand{display:flex;align-items:center;gap:10px;font-weight:600;color:var(--gold);font-size:32px}
.brand-dot{width:18px;height:18px;border-radius:50%;background:var(--gold)}
.nav{top:52px;font-size:13px;font-weight:500}
.nav.active{color:var(--gold)}
.btn-pill{border-radius:28px}

/* hero */
.hero-photo{left:0;top:122px;width:1200px;height:636px;background:linear-gradient(90deg,#c9b48a 0%,#d9d2c4 30%,#a9a398 60%,#8d8a84 100%)}
.hero-panel{left:648px;top:222px;width:488px;height:440px;border-radius:20px;background:rgba(20,20,20,.82)}
.hero-title{left:648px;width:488px;top:316px;text-align:center;font-family:"Montserrat Alternates",sans-serif;font-size:50px;line-height:48px;color:transparent;-webkit-text-stroke:1.4px #fff}
.hero-text{left:680px;width:424px;top:440px;text-align:center;font-size:14px;line-height:24px}

/* services */
.service-card{position:absolute;width:452px;height:318px;border-radius:6px;overflow:hidden}
.service-card .shade{position:absolute;inset:0;background:linear-gradient(180deg,rgba(0,0,0,0) 55%,rgba(201,160,44,.85) 100%)}
.service-card span{position:absolute;left:0;right:0;bottom:12px;text-align:center;color:#1a1200;font-weight:600;font-size:18px}

/* about */
.about-bg{left:0;top:1950px;width:1200px;height:666px;background:#030303}
.lead{left:70px;width:456px;top:2154px;font-weight:700;font-size:19px;line-height:32px;text-align:justify}
.body-copy{left:70px;width:456px;top:2226px;font-size:13px;line-height:27px;text-align:justify}
.ring{position:absolute;width:508px;height:508px;border-radius:50%;border:2px solid var(--gold)}
.ring .photo{position:absolute;left:20px;top:20px;width:464px;height:464px;border-radius:50%;background:linear-gradient(160deg,#9aa3ad 0%,#c4a44a 55%,#e07a1a 80%,#e8e6e0 100%)}

/* testimonials */
.testi-bg{left:0;top:2616px;width:1200px;height:742px;background:var(--panel)}
.quote-text{left:240px;width:720px;top:3020px;text-align:center;font-style:italic;font-size:17px;line-height:30px}

/* cta */
.cta-bg{left:0;top:3358px;width:1200px;height:574px;background:linear-gradient(180deg,#2a2826 0%,#3a3630 50%,#1d1c1a 100%)}
.cta-title{top:3512px;font-weight:700;font-size:66px;line-height:70px;letter-spacing:-.5px}
.cta-text{left:190px;width:820px;top:3672px;text-align:center;font-size:14px;line-height:24px}

/* contact */
.field{position:absolute;background:#fff;color:#9a9a9a;font-size:13px;padding:13px 18px}

/* footer */
.footer-bg{left:0;top:4676px;width:1200px;height:474px;background:var(--panel)}
.footer-head{top:4800px;font-weight:600;font-size:24px}
.footer-link{font-size:14px;display:flex;align-items:center;gap:12px}
.footer-link::before{content:"";width:7px;height:7px;border-radius:50%;background:var(--gold)}
.ico{width:36px;height:36px;border-radius:50%;background:var(--gold);display:flex;align-items:center;justify-content:center}
.contact-line{font-size:14px;line-height:24px}
</style>
</head>
<body>

<!-- Header -->
<div class="abs site-header"></div>
<div class="abs brand" style="left:72px;top:44px"><span class="brand-dot"></span>Kestrim</div>
<div class="abs nav active" style="left:494px">HOME</div>
<div class="abs nav" style="left:566px">ABOUT US</div>
<div class="abs nav" style="left:666px">SERVICES</div>
<div class="abs nav" style="left:760px">CLIENTS</div>
<div class="abs nav" style="left:842px">CONTACT US</div>
<div class="btn btn-pill" style="left:964px;top:36px;width:174px;height:52px">CONTACT US</div>

<!-- Hero -->
<div class="abs hero-photo" role="img" aria-label="Two construction professionals in hard hats reviewing plans on a building site"></div>
<div class="abs hero-panel"></div>
<div class="abs hero-title">WE BUILD<br>YOUR DREAM</div>
<div class="abs hero-text">Lorem ipsum dolor sit amet, consectetur adipiscing elit, sed do eiusmod tempor incididunt ut labore et dolore magna</div>
<div class="btn" style="left:804px;top:512px;width:176px;height:52px">CONTACT US</div>

<!-- Services -->
<div class="section-title center" style="top:890px">OUR SERVICES</div>
<div class="rule" style="left:558px;top:956px"></div>

<div class="service-card" style="left:126px;top:1026px;background:linear-gradient(150deg,#b9b3a7,#d97a2a 60%,#6d5b3e)" role="img" aria-label="Contractors reviewing plans together on site">
  <div class="shade"></div><span>GENERAL CONTRACTING</span></div>
<div class="service-card" style="left:630px;top:1026px;background:linear-gradient(150deg,#3a2a2a,#e8e4dc 50%,#bdb6aa)" role="img" aria-label="Hands drafting architectural plans">
  <div class="shade"></div><span>DESIGN-BUILD CONSTRUCTION</span></div>
<div class="service-card" style="left:126px;top:1386px;background:linear-gradient(150deg,#6b6a4a,#4a4a38 50%,#8c8460)" role="img" aria-label="Aerial view of flood-damaged land">
  <div class="shade"></div><span>DISASTER RECOVERY</span></div>
<div class="service-card" style="left:630px;top:1386px;background:linear-gradient(150deg,#c8c8c8,#8c8c8c 50%,#d6d44a)" role="img" aria-label="Engineer in safety vest beside a river">
  <div class="shade"></div><span>ENVIRONMENTAL REMEDIATION</span></div>

<div class="btn" style="left:500px;top:1778px;width:200px;height:54px;font-size:12px">VIEW ALL SERVICES</div>

<!-- About -->
<div class="abs about-bg"></div>
<div class="section-title" style="left:70px;top:2058px">ABOUT US</div>
<div class="rule" style="left:72px;top:2114px"></div>
<div class="abs lead">Lorem ipsum dolor sit amet, consectetur adipiscing elit,</div>
<div class="abs body-copy">sed do eiusmod tempor incididunt ut labore et dolore magna aliqua. Ut enim ad minim veniam, quis nostrud exercitation ullamco laboris nisi ut aliquip ex ea commodo consequat. Duis aute irure dolor in reprehenderit in voluptate velit esse cillum dolore eu fugiat nulla pariatur. Excepteur sint occaecat cupidatat non proident, sunt in culpa qui officia deserunt mollit anim id est laborum.</div>
<div class="btn" style="left:70px;top:2422px;width:176px;height:52px">CONTACT US</div>
<div class="ring" style="left:608px;top:2030px"><div class="photo" role="img" aria-label="Two engineers in hard hats reviewing drawings in front of high-rise buildings"></div></div>

<!-- Testimonials -->
<div class="abs testi-bg"></div>
<div class="section-title center" style="top:2748px">OUR TESTIMONIALS</div>
<div class="rule" style="left:558px;top:2816px"></div>
<svg class="abs" style="left:554px;top:2892px" width="94" height="76" viewBox="0 0 94 76" aria-hidden="true">
  <g fill="#d4a829">
    <circle cx="20" cy="54" r="20"/><path d="M2 52 C2 24 14 6 34 0 L38 8 C24 14 18 26 20 40 Z"/>
    <circle cx="72" cy="54" r="20"/><path d="M54 52 C54 24 66 6 86 0 L90 8 C76 14 70 26 72 40 Z"/>
  </g>
</svg>
<svg class="abs" style="left:140px;top:3040px" width="24" height="34" viewBox="0 0 24 34" aria-hidden="true"><path d="M20 3 L5 17 L20 31" fill="none" stroke="#fff" stroke-width="4"/></svg>
<svg class="abs" style="left:1038px;top:3040px" width="24" height="34" viewBox="0 0 24 34" aria-hidden="true"><path d="M4 3 L19 17 L4 31" fill="none" stroke="#fff" stroke-width="4"/></svg>
<div class="abs quote-text">Lorem ipsum dolor sit amet, consectetur adipiscing elit, sed do eiusmod tempor incididunt ut labore et dolore magna aliqua. Ut enim ad minim veniam, quis nostrud exercitation ullamco laboris .</div>
<div class="abs center" style="top:3146px;font-weight:600;font-size:22px">DANIEL MORROW</div>
<div class="abs center" style="top:3176px;font-size:26px;color:var(--gold);letter-spacing:4px">★★★★★</div>

<!-- CTA -->
<div class="abs cta-bg" role="img" aria-label="Dimmed view of a house under construction"></div>
<div class="abs center cta-title">WE WORK WITH YOU FROM<br>DESIGN TO CONSTRUCTION</div>
<div class="abs cta-text">Lorem ipsum dolor sit amet, consectetur adipiscing elit, sed do eiusmod tempor incididunt ut labore et dolore magna aliqua.  Quis ipsum suspendisse ultrices gravida. Risus commodo viverra maecenas accumsan lacus vel facilisis.</div>
<div class="btn" style="left:500px;top:3756px;width:176px;height:54px">CONTACT US</div>

<!-- Contact -->
<div class="section-title" style="left:70px;top:4094px">CONTACT US</div>
<div class="rule" style="left:72px;top:4154px"></div>
<div class="field" style="left:70px;top:4216px;width:222px;height:46px">First Name:</div>
<div class="field" style="left:312px;top:4216px;width:222px;height:46px">Last Name:</div>
<div class="field" style="left:70px;top:4280px;width:222px;height:46px">Phone:</div>
<div class="field" style="left:312px;top:4280px;width:222px;height:46px">Email:</div>
<div class="field" style="left:70px;top:4346px;width:464px;height:142px">Mesage:</div>
<div class="btn" style="left:70px;top:4538px;width:176px;height:44px">SUBMIT A MESSAGE</div>
<div class="ring" style="left:608px;top:4096px"><div class="photo" role="img" aria-label="Two engineers in hard hats reviewing drawings in front of high-rise buildings"></div></div>

<!-- Footer -->
<div class="abs footer-bg"></div>
<div class="abs brand" style="left:184px;top:4850px"><span class="brand-dot"></span>Kestrim</div>
<div class="abs ico" style="left:208px;top:4948px" role="img" aria-label="Social profile"></div>
<div class="abs ico" style="left:256px;top:4948px" role="img" aria-label="Social profile"></div>
<div class="abs ico" style="left:304px;top:4948px" role="img" aria-label="Social profile"></div>

<div class="abs footer-head" style="left:550px">LINKS</div>
<div class="rule" style="left:552px;top:4836px;width:64px"></div>
<div class="abs footer-link" style="left:552px;top:4874px">About Us</div>
<div class="abs footer-link" style="left:552px;top:4906px">Services</div>
<div class="abs footer-link" style="left:552px;top:4938px">Clients</div>
<div class="abs footer-link" style="left:552px;top:4970px">Contact Us</div>

<div class="abs footer-head" style="left:822px">CONTACT US</div>
<div class="rule" style="left:824px;top:4836px;width:64px"></div>
<div class="abs ico" style="left:826px;top:4862px"><svg width="16" height="20" viewBox="0 0 16 20"><path d="M8 1a6 6 0 0 0-6 6c0 5 6 12 6 12s6-7 6-12a6 6 0 0 0-6-6z" fill="#111"/><circle cx="8" cy="7" r="2.3" fill="#d4a829"/></svg></div>
<div class="abs contact-line" style="left:874px;top:4864px">Lorem ipsum,Lorem ipsum.<br>Lorem ipsum</div>
<div class="abs ico" style="left:826px;top:4932px"><svg width="18" height="18" viewBox="0 0 24 24"><path d="M6.6 10.8a15 15 0 0 0 6.6 6.6l2.2-2.2a1 1 0 0 1 1-.25 11 11 0 0 0 3.6.6 1 1 0 0 1 1 1V20a1 1 0 0 1-1 1A17 17 0 0 1 3 4a1 1 0 0 1 1-1h3.5a1 1 0 0 1 1 1 11 11 0 0 0 .6 3.6 1 1 0 0 1-.25 1z" fill="#111"/></svg></div>
<div class="abs contact-line" style="left:874px;top:4938px">(987) 654 3210</div>
<div class="abs ico" style="left:826px;top:4986px"><svg width="18" height="14" viewBox="0 0 18 14"><rect x="1" y="1" width="16" height="12" rx="1.5" fill="#111"/><path d="M1.5 2 L9 8 L16.5 2" fill="none" stroke="#d4a829" stroke-width="1.4"/></svg></div>
<div class="abs contact-line" style="left:874px;top:4992px">info@companyname.com</div>

<div class="abs" style="left:70px;top:5070px;width:1066px;height:1px;background:#8a8a8a"></div>
<div class="abs center" style="top:5100px;font-size:14px">Copyright © 2025 All Rights Reserved By Company Name</div>

</body>
</html>
```